Pine Ridge Traders, LLC- Global Beverage Company with 100% Cold Chain Logistics

Hey All, My Name is Tom, I am a young business owner in a competitive export space, but my niche is that I am shipping all of my beer around the world, "100% Cold Chain". This model is more costly, but it protects the integrity of the beer itself and will give folks in foreign countries the best representation of what US Craft Beer has to offer.

I am not a branding guy and don't claim to be one, I am a salesperson first, and will be referring to all of you to create something great that will be memorable.

I am looking for a basic Business Card Design for my Craft Beer Export company. I sell US Craft Beer in several countries around the globe. Austrailia, China, Taiwan, Chile, France, New Zealand... to name a few.

I am looking for a sleek, modern, and fresh design. Quickly!

Thanks for your consideration!

Cheers,

Tom

Target Market(s)

International

Contact Information for Business Card

Tom Reilly
Founder- World Brew Guy
Tom@PineRidgeTraders.example
@WorldBrewGuy- Instagram only
www.Pineridgetraders.example
@PineRidgeTradersAU- Instagram Only

Font styles to use
Serif

Colors
0592cd
ffffff

Requirements
Must have
• Name-
• Title-
• Email-
• Social Media Handle-
• Company Website-
Nice to have
• Nice Logo/ Images on Card
Should not have
• Tacky Beer Images

```html
<!DOCTYPE html>
<html lang="en">
<head>
<meta charset="utf-8">
<title>Pine Ridge Traders – Business Card</title>
<link rel="stylesheet" href="https://fonts.googleapis.com/css2?family=Courier+Prime&family=Arimo&family=PT+Serif&family=PT+Sans&display=swap">
<style>
  :root {
    --ink: #000000;
    --paper: #ffffff;
    --brand-blue: #0592cd;
    --mark-grey: #555555;
    --rule-grey: #b5b5b5;
    --text-dark: #111111;
  }
  html, body {
    margin: 0;
    padding: 0;
    width: 1200px;
    height: 1130px;
    overflow: hidden;
    background: var(--paper);
  }
  .canvas {
    position: relative;
    width: 1200px;
    height: 1130px;
  }
  .card {
    position: absolute;
    left: 0;
    width: 1200px;
    background: var(--ink);
  }
  .card--front { top: 10px; height: 535px; }
  .card--back  { top: 592px; height: 538px; }

  .contact-panel {
    position: absolute;
    left: 28px;
    top: 13px;
    width: 637px;
    height: 495px;
    background: var(--paper);
  }
  .contact-panel__name {
    position: absolute;
    left: 22px;
    top: 52px;
    margin: 0;
    font: 400 42px/1 "Courier Prime", monospace;
    color: var(--text-dark);
  }
  .contact-panel__rule {
    position: absolute;
    left: 22px;
    top: 102px;
    width: 445px;
    height: 2px;
    background: var(--rule-grey);
  }
  .contact-panel__title {
    position: absolute;
    left: 22px;
    top: 112px;
    margin: 0;
    font: 400 25px/1.2 "PT Serif", serif;
    color: var(--text-dark);
  }
  .contact-list {
    position: absolute;
    left: 22px;
    top: 212px;
    margin: 0;
    padding: 0;
    list-style: none;
  }
  .contact-list__item {
    display: flex;
    align-items: center;
    height: 32px;
    margin-bottom: 31px;
    font: 400 26px/1 "Arimo", sans-serif;
    color: var(--text-dark);
  }
  .contact-list__icon {
    width: 28px;
    height: 28px;
    margin-right: 18px;
    flex: none;
  }

  .accent-bar {
    position: absolute;
    left: 706px;
    top: 13px;
    width: 33px;
    height: 495px;
    background: var(--brand-blue);
  }
  .brand-mark {
    position: absolute;
    left: 770px;
    top: 150px;
    width: 400px;
    display: flex;
    align-items: center;
    justify-content: center;
    gap: 22px;
  }
  .brand-mark__dot {
    width: 58px;
    height: 58px;
    border-radius: 50%;
    background: var(--mark-grey);
    flex: none;
  }
  .brand-mark__name {
    font: 400 44px/1.05 "PT Sans", sans-serif;
    color: var(--mark-grey);
  }

  .back-frame {
    position: absolute;
    left: 28px;
    top: 20px;
    width: 1121px;
    height: 473px;
    border: 12px solid var(--brand-blue);
  }
  .back-frame__halo {
    position: absolute;
    left: 430px;
    top: 40px;
    width: 330px;
    height: 330px;
    border-radius: 50%;
    background: #1e1e1e;
  }
  .back-frame__name {
    position: absolute;
    left: 0;
    right: 0;
    top: 208px;
    margin: 0;
    text-align: center;
    font: 400 66px/1 "PT Sans", sans-serif;
    letter-spacing: 2px;
    color: var(--paper);
  }
  .back-frame__underline {
    position: absolute;
    left: 212px;
    top: 293px;
    width: 696px;
    height: 5px;
    background: var(--brand-blue);
  }
</style>
</head>
<body>
<div class="canvas">
  <section class="card card--front">
    <div class="contact-panel">
      <h1 class="contact-panel__name">Tom Reilly</h1>
      <div class="contact-panel__rule"></div>
      <p class="contact-panel__title">Founder of World Brew Guy</p>
      <ul class="contact-list">
        <li class="contact-list__item">
          <svg class="contact-list__icon" viewBox="0 0 28 28" aria-hidden="true">
            <circle cx="14" cy="14" r="12.5" fill="none" stroke="#111" stroke-width="1.6"/>
            <rect x="7" y="9.5" width="14" height="9" fill="none" stroke="#111" stroke-width="1.6"/>
            <path d="M7 9.5 L14 15 L21 9.5" fill="none" stroke="#111" stroke-width="1.6"/>
          </svg>
          Tom@PineRidgeTraders.example
        </li>
        <li class="contact-list__item">
          <svg class="contact-list__icon" viewBox="0 0 28 28" aria-hidden="true">
            <circle cx="14" cy="14" r="12.5" fill="none" stroke="#111" stroke-width="1.6"/>
            <circle cx="14" cy="14" r="7" fill="none" stroke="#111" stroke-width="1.4"/>
            <ellipse cx="14" cy="14" rx="3" ry="7" fill="none" stroke="#111" stroke-width="1.4"/>
            <line x1="7" y1="14" x2="21" y2="14" stroke="#111" stroke-width="1.4"/>
          </svg>
          www.Pineridgetraders.example
        </li>
        <li class="contact-list__item">
          <svg class="contact-list__icon" viewBox="0 0 28 28" aria-hidden="true">
            <circle cx="14" cy="14" r="12.5" fill="none" stroke="#111" stroke-width="1.6"/>
          </svg>
          @WorldBrewGuy
        </li>
        <li class="contact-list__item">
          <svg class="contact-list__icon" viewBox="0 0 28 28" aria-hidden="true">
            <circle cx="14" cy="14" r="12.5" fill="none" stroke="#111" stroke-width="1.6"/>
          </svg>
          @PineRidgeTradersAU
        </li>
      </ul>
    </div>
    <div class="accent-bar"></div>
    <div class="brand-mark">
      <span class="brand-mark__dot"></span>
      <span class="brand-mark__name">Pine Ridge<br>Traders</span>
    </div>
  </section>

  <section class="card card--back">
    <div class="back-frame">
      <div class="back-frame__halo"></div>
      <h2 class="back-frame__name">PINE RIDGE TRADERS</h2>
      <div class="back-frame__underline"></div>
    </div>
  </section>
</div>
</body>
</html>
```